Financial Planning Business needs a business card design

We need a business card design that is for a new financial planning business based in Australia. We provide financial planning advice such as retirement planning, wealth creation, asset protection.

Attached is the logo design. On the front side of the business card needs to incorporate the following:
- adviser name
- adviser title (ie Managing Director)
- address
- phone number
- email
- website address

Ideally it should also have the business name and logo

On the back of the card I would like this to be black in colour with the business name and logo

I have been advised the font is "Cinzel" (regular and bold)

Industry/Entity Type

Financial

Requirements
Must have
• Logo and business name

Format to have as follows:
Tom xxxxxxxx
Managing Director / Senior Financial Adviser
address
phone email
website

```html
<!DOCTYPE html>
<html lang="en">
<head>
<meta charset="utf-8">
<title>Keystone Wealth Planning – Business Card</title>
<link rel="stylesheet" href="https://fonts.googleapis.com/css2?family=Gelasio:ital,wght@0,400;0,700;1,400&display=swap">
<style>
  :root {
    --band-dark: #757577;
    --band-light: #c8c8c8;
    --paper: #ffffff;
    --ink: #111111;
    --brand-blue: #1c9fd2;
    --mark-grey: #8a8a8c;
  }
  * { margin: 0; padding: 0; box-sizing: border-box; }
  html, body {
    width: 1200px;
    height: 741px;
    overflow: hidden;
    background: var(--paper);
  }
  .card {
    position: relative;
    width: 1200px;
    height: 741px;
    background: var(--paper);
    font-family: "Gelasio", Georgia, serif;
    color: var(--ink);
  }
  .band-top {
    position: absolute;
    left: 0; top: 0;
    width: 1200px; height: 86px;
    background: var(--band-dark);
  }
  .band-bottom {
    position: absolute;
    left: 0; top: 576px;
    width: 1200px; height: 165px;
    background: var(--band-light);
  }
  .panel {
    position: absolute;
    left: 130px; top: 65px;
    width: 940px; height: 546px;
    background: var(--paper);
  }
  .brand {
    position: absolute;
    left: 186px; top: 112px;
    display: flex;
    align-items: center;
    gap: 34px;
  }
  .brand-square {
    width: 150px; height: 150px;
    background: var(--mark-grey);
  }
  .brand-name {
    font-weight: 400;
    font-size: 66px;
    line-height: 1.08;
    color: var(--brand-blue);
  }
  .adviser {
    position: absolute;
    left: 415px; top: 330px;
    font-weight: 700;
    font-size: 30px;
    line-height: 38px;
  }
  .contact {
    position: absolute;
    left: 415px; top: 446px;
    list-style: none;
    font-size: 26px;
    line-height: 32px;
  }
  .tagline {
    position: absolute;
    left: 0; top: 652px;
    width: 1200px;
    text-align: center;
    font-style: italic;
    font-size: 21px;
  }
</style>
</head>
<body>
  <div class="card">
    <div class="band-top"></div>
    <div class="band-bottom"></div>
    <div class="panel"></div>

    <div class="brand">
      <div class="brand-square"></div>
      <div class="brand-name">Keystone<br>Wealth Planning</div>
    </div>

    <div class="adviser">
      <div class="adviser-name">Tom xxxxxxxx</div>
      <div class="adviser-title">Managing Director</div>
    </div>

    <ul class="contact">
      <li>address</li>
      <li>phone</li>
      <li>email</li>
      <li>website</li>
    </ul>

    <p class="tagline">We provide financial planning advice for retirement planning, wealth creation, asset protection and more.</p>
  </div>
</body>
</html>
```